Interior Design & Furniture E commerce Website Design

I need a cutting edge website design, this is for Interior Design Services as well as eCommerce for furniture and home decor www.lorivelhomestudio.com
Here is a sample of the concept behind the site.
I am a furniture & Interior Designer, want to create a life style brand.
Will offer Interior Design Services : Commercial & Residential (this portion will be a catalog or portfolio type)
The eCommerce side will sell, Furniture, Lighting, Decor, Gifts, Textiles, will also be offering trade so that could be at bottom of site. I also like the concept of concierge as where all the info falls under: shipping, etc..

*Please make sure to make the eCommerce prominent.

Hello Designers, I also would like to possibly update my logo, the current one I like but don't Love.

Target Market(s)

High end customers with disposable income, who also appreciate quality and unique furniture & design

Number of Pages Required

5+ page

Colors
0255a3
f37122

Requirements
Must have
• Room Planer: I will be using this tool http://qtstudio.varnelbex.com/room-planner.inc
• Live Chat
• Will be offering 3d renderings for spaces as well as Virtual Reality
• The image I loaded that looks like copper, I would like to have that as a color on the site with the texture: so the colors are Blue and copper. Would like the site to be user friendly and interactive
• http://qtstudio.varnelbex.com/ (this is the current site in development, so we will be offering Design your own, Trends, inspiration, etc...
• I have included a headshot to use for now about me. or about us.
• I also included several actual project installation (residential and commercial) as well as a variety of my furniture items
• I have Included an old Bio and some articles I would like to show case in a Press Area
• I would also like to include a section for Events (Giving back )I do a lot of charity events 1-2 a year and would like to showcase that as well
• *Please make the store (ecommerce prominent )

```html
<!DOCTYPE html>
<html lang="en">
<head>
<meta charset="utf-8">
<title>Lorivel Home Studio — Furniture &amp; Interior Design</title>
<link href="https://fonts.googleapis.com/css2?family=Montserrat:wght@300;400;500;600&family=Open+Sans:wght@400;600;700&display=swap" rel="stylesheet">
<style>
:root{
  --copper:#b8652c;
  --copper-light:#d08a4f;
  --brown-dark:#2e1b13;
  --brown-mid:#4a2c1d;
  --ink:#333;
  --muted:#777;
  --line:#e2e2e2;
  --footer:#3b3b3b;
  --white:#fff;
  --star:#e8a33c;
}
*{box-sizing:border-box;margin:0;padding:0}
html,body{width:1200px;height:4080px;overflow:hidden}
body{font-family:"Open Sans",Arial,sans-serif;color:var(--ink);background:var(--white);font-size:14px}
.section-title{font-family:"Montserrat",Arial,sans-serif;font-weight:300;text-transform:uppercase;letter-spacing:3px;font-size:32px;text-align:center}
.section-title.light{color:var(--white)}
.title-rule{display:block;width:70px;height:2px;background:var(--copper);margin:14px auto 0}
.btn{display:inline-block;background:var(--copper);color:var(--white);font-family:"Montserrat",Arial,sans-serif;font-size:11px;font-weight:500;letter-spacing:1.5px;text-transform:uppercase;padding:12px 24px;text-decoration:none}

/* Header */
.site-header{height:120px;display:flex;align-items:center;padding:0 80px;border-bottom:1px solid var(--line)}
.brand{display:flex;flex-direction:column;align-items:center;gap:6px;width:110px}
.brand-mark{width:48px;height:48px;background:var(--copper)}
.brand-name{font-family:"Montserrat",Arial,sans-serif;font-size:10px;font-weight:500;letter-spacing:1.5px;color:var(--copper);text-transform:uppercase;text-align:center;line-height:1.3}
.main-nav{display:flex;gap:36px;margin-left:auto;margin-right:90px;font-family:"Montserrat",Arial,sans-serif;font-size:12px;font-weight:500;letter-spacing:1px}
.main-nav a{color:var(--ink);text-decoration:none}
.header-tools{display:flex;align-items:center;gap:22px;font-size:12px}
.header-tools span{display:flex;align-items:center;gap:6px}

/* Hero */
.hero{height:380px;position:relative;display:flex;align-items:center;justify-content:center;overflow:hidden}
.hero-photo{position:absolute;inset:0;background:
  radial-gradient(ellipse 35% 55% at 22% 45%,rgba(214,160,110,.55),transparent 70%),
  radial-gradient(ellipse 30% 50% at 78% 40%,rgba(200,140,95,.45),transparent 70%),
  linear-gradient(180deg,#2b1d17 0%,#5c4030 40%,#7a5843 60%,#2a1c16 100%)}
.hero-photo::after{content:"";position:absolute;inset:0;background:rgba(30,18,12,.35)}
.hero-title{position:relative;font-family:"Montserrat",Arial,sans-serif;font-weight:300;color:var(--white);font-size:68px;letter-spacing:8px;text-align:center;line-height:1.05;text-transform:uppercase}

/* Promise strip */
.promises{height:50px;display:flex;justify-content:center;gap:170px;align-items:center;border-bottom:1px solid var(--line);box-shadow:0 3px 6px rgba(0,0,0,.08);position:relative}
.promise{display:flex;align-items:center;gap:10px;font-family:"Montserrat",Arial,sans-serif;font-size:10px;font-weight:600;letter-spacing:.5px;line-height:1.3;text-transform:uppercase}
.promise small{display:block;font-weight:400;color:var(--muted)}

/* About */
.about{height:510px;display:flex;padding:64px 80px 0 80px;gap:60px}
.about-portrait{position:relative;width:250px;height:300px;flex:none}
.about-portrait .frame{position:absolute;left:18px;top:18px;width:250px;height:300px;border:2px solid var(--copper)}
.about-portrait .photo{position:absolute;inset:0;background:
  radial-gradient(ellipse 45% 40% at 55% 42%,#cfcfcf,transparent 72%),
  linear-gradient(160deg,#f1f1f1 0%,#bdbdbd 45%,#5e5e5e 100%)}
.about-body h2{font-family:"Montserrat",Arial,sans-serif;font-weight:400;font-size:32px;letter-spacing:3px;padding-bottom:10px;border-bottom:2px solid var(--copper);display:inline-block;padding-right:200px}
.about-body p{margin:22px 0 28px;font-size:14px;line-height:1.85;color:#555}

/* Services */
.services{height:400px;background:
  radial-gradient(ellipse 40% 60% at 20% 50%,rgba(140,90,55,.35),transparent 70%),
  radial-gradient(ellipse 40% 60% at 80% 50%,rgba(140,90,55,.3),transparent 70%),
  linear-gradient(180deg,var(--brown-mid),var(--brown-dark));padding-top:52px}
.service-list{display:flex;justify-content:center;gap:62px;margin-top:40px}
.service{width:150px;text-align:center;color:var(--white);font-size:13px;line-height:1.45}
.service .thumb{width:124px;height:124px;border-radius:50%;margin:0 auto 16px;border:3px solid rgba(255,255,255,.35)}

/* Catalogue */
.catalogue{height:500px;padding-top:56px}
.tabs{display:flex;justify-content:center;gap:42px;margin-top:30px;font-family:"Montserrat",Arial,sans-serif;font-size:11px;letter-spacing:1px;text-transform:uppercase}
.tabs .active{color:var(--copper);border-bottom:2px solid var(--copper);padding-bottom:4px}
.carousel{display:flex;align-items:center;justify-content:center;gap:40px;margin-top:34px}
.arrow{width:24px;height:24px}
.cat-card{width:212px;text-align:center}
.cat-card .thumb{height:170px;border:1px solid var(--line);box-shadow:0 2px 6px rgba(0,0,0,.1);display:flex;align-items:center;justify-content:center;background:#fafafa}
.cat-card .thumb div{width:170px;height:100px;background:linear-gradient(180deg,#c7c2ba 0%,#8f877c 55%,#4e4842 100%)}
.cat-card p{margin-top:14px;font-family:"Montserrat",Arial,sans-serif;font-size:12px;font-weight:500;letter-spacing:1px}

/* Interior design */
.interiors{height:510px;background:
  radial-gradient(ellipse 50% 60% at 50% 40%,rgba(120,75,45,.4),transparent 70%),
  linear-gradient(180deg,var(--brown-dark),var(--brown-mid) 50%,var(--brown-dark));padding-top:46px;text-align:center}
.interior-list{display:flex;justify-content:center;gap:30px;margin-top:34px}
.interior-card{width:510px;background:var(--white)}
.interior-card .photo{height:210px}
.interior-card p{height:44px;line-height:44px;color:var(--copper);font-family:"Montserrat",Arial,sans-serif;font-size:20px;letter-spacing:2px;text-transform:uppercase}
.interiors .btn{margin-top:32px}

/* Featured */
.featured{height:450px;padding-top:56px}
.featured .section-title{color:var(--copper)}
.product-list{display:flex;justify-content:center;gap:24px;margin-top:36px}
.product{width:150px;text-align:center;font-size:12px}
.product .thumb{height:150px;border:1px solid var(--line);display:flex;align-items:center;justify-content:center}
.product .thumb div{width:104px;height:94px}
.product .label{margin-top:12px;color:var(--muted);font-size:11px}
.product .price{margin-top:4px}
.product .price s{color:#aaa;margin-right:6px}
.product .price b{color:var(--copper)}
.stars{margin-top:4px;color:var(--star);letter-spacing:2px;font-size:13px}

/* Events */
.events{height:460px;border-top:1px solid var(--line);padding-top:52px;text-align:center}
.events .section-title{color:var(--copper)}
.event-list{display:flex;justify-content:center;gap:60px;margin-top:32px;text-align:left}
.event{display:flex;width:460px;gap:18px}
.event .photo{width:200px;height:200px;position:relative;flex:none}
.event .date{position:absolute;right:0;top:0;width:58px;height:86px;background:var(--copper);color:var(--white);text-align:center;font-family:"Montserrat",Arial,sans-serif;padding-top:6px;font-size:11px;line-height:1.2}
.event .date b{display:block;font-size:30px;font-weight:600}
.event h3{font-family:"Montserrat",Arial,sans-serif;font-size:17px;font-weight:600;line-height:1.3}
.event p{margin:10px 0;color:#555;line-height:1.6;font-size:13px}
.event a{color:var(--copper);font-weight:700;text-decoration:none;font-size:13px}
.events .btn{margin-top:28px}

/* Contact */
.contact{height:540px;background:
  radial-gradient(ellipse 45% 50% at 30% 30%,rgba(110,65,40,.35),transparent 70%),
  linear-gradient(180deg,var(--brown-dark),#22150f);padding:52px 90px 0;color:var(--white)}
.contact-intro{text-align:center;max-width:780px;margin:24px auto 0;font-size:13px;line-height:1.7;color:#e6d9d0}
.form-row{display:flex;gap:40px;margin-top:48px}
.field{flex:1;border-bottom:1px solid rgba(255,255,255,.6);padding-bottom:10px;font-size:12px}
.field.select{display:flex;justify-content:space-between;align-items:center}
.message{margin-top:30px;height:100px;border-bottom:1px solid rgba(255,255,255,.6);font-size:12px}
.contact .submit{text-align:center;margin-top:32px}
.contact .btn{padding:12px 46px}

/* Footer */
.site-footer{height:160px;background:var(--footer);text-align:center;padding-top:40px}
.social{display:flex;justify-content:center;gap:16px}
.social span{width:42px;height:42px;border-radius:50%;border:2px solid var(--white);display:flex;align-items:center;justify-content:center}
.site-footer p{margin-top:22px;font-size:11px;color:#bbb}
</style>
</head>
<body>

<header class="site-header">
  <div class="brand">
    <span class="brand-mark"></span>
    <span class="brand-name">Lorivel Home Studio</span>
  </div>
  <nav class="main-nav">
    <a href="#">HOME</a><a href="#">ABOUT</a><a href="#">SERVICES</a><a href="#">SHOP</a><a href="#">CONTACT</a><a href="#">BLOG</a>
  </nav>
  <div class="header-tools">
    <svg width="16" height="16" viewBox="0 0 16 16"><circle cx="6.5" cy="6.5" r="5" fill="none" stroke="#333" stroke-width="1.6"/><line x1="10.3" y1="10.3" x2="15" y2="15" stroke="#333" stroke-width="1.8"/></svg>
    <span><svg width="16" height="14" viewBox="0 0 16 14"><path d="M1 1h2.5l2 8h8l2-6H4.5" fill="none" stroke="#333" stroke-width="1.4"/><circle cx="6.5" cy="12" r="1.2" fill="#333"/><circle cx="12.5" cy="12" r="1.2" fill="#333"/></svg>My Basket</span>
    <span><svg width="14" height="14" viewBox="0 0 14 14"><circle cx="7" cy="4" r="3" fill="none" stroke="#333" stroke-width="1.4"/><path d="M1 14c0-4 3-5.5 6-5.5s6 1.5 6 5.5" fill="none" stroke="#333" stroke-width="1.4"/></svg>Login</span>
  </div>
</header>

<section class="hero">
  <div class="hero-photo" role="img" aria-label="Furniture showroom interior with warm lighting"></div>
  <h1 class="hero-title">Best Furniture<br>Design</h1>
</section>

<section class="promises">
  <div class="promise">
    <svg width="26" height="26" viewBox="0 0 26 26"><circle cx="13" cy="13" r="12" fill="none" stroke="#b8652c" stroke-width="1.6"/><text x="13" y="17.5" text-anchor="middle" font-size="13" fill="#b8652c" font-family="Montserrat">$</text></svg>
    <div>100% Money Back<small>Guarantee</small></div>
  </div>
  <div class="promise">
    <svg width="30" height="22" viewBox="0 0 30 22"><rect x="1" y="3" width="17" height="12" fill="none" stroke="#b8652c" stroke-width="1.6"/><path d="M18 7h6l4 4v4H18z" fill="none" stroke="#b8652c" stroke-width="1.6"/><circle cx="7" cy="18" r="2.5" fill="#b8652c"/><circle cx="23" cy="18" r="2.5" fill="#b8652c"/></svg>
    <div>Free Shipping</div>
  </div>
  <div class="promise">
    <svg width="26" height="26" viewBox="0 0 26 26"><path d="M4 15v-3a9 9 0 0 1 18 0v3" fill="none" stroke="#b8652c" stroke-width="1.6"/><rect x="2" y="14" width="5" height="7" fill="#b8652c"/><rect x="19" y="14" width="5" height="7" fill="#b8652c"/></svg>
    <div>24 - Hour<small>Active Support</small></div>
  </div>
</section>

<section class="about">
  <div class="about-portrait">
    <div class="frame"></div>
    <div class="photo" role="img" aria-label="Black and white portrait photo of the designer"></div>
  </div>
  <div class="about-body">
    <h2>ABOUT</h2>
    <p>As a child, our founder spent quiet weekends in her family's furniture workshop, sketching chairs and learning how fine pieces come together. That early curiosity became a lifelong passion for craft, proportion and warm, livable rooms. After years designing hospitality interiors and custom collections, she opened a studio devoted to furniture and spaces that are both beautiful and built to last. Today the studio creates residential and commercial projects for clients who value quality and unique design.</p>
    <a class="btn" href="#">Read More</a>
  </div>
</section>

<section class="services">
  <h2 class="section-title light">Services</h2>
  <div class="service-list">
    <div class="service"><div class="thumb" style="background:radial-gradient(circle at 40% 35%,#e2cba9,#9a7650 55%,#4f3822)" role="img" aria-label="Custom furniture piece"></div>Custom Designed Furniture from concept to production</div>
    <div class="service"><div class="thumb" style="background:conic-gradient(#d94b3b,#f0b23c,#5aa45b,#3c7cc5,#8a4fb3,#d94b3b)" role="img" aria-label="Colour swatch fan"></div>Color Schemes</div>
    <div class="service"><div class="thumb" style="background:radial-gradient(circle at 40% 35%,#c9ae8c,#7d6247 55%,#3e2e20)" role="img" aria-label="Fabric samples"></div>Fabric Selections</div>
    <div class="service"><div class="thumb" style="background:radial-gradient(circle at 40% 35%,#f4ece0,#c2b199 55%,#7d6b55)" role="img" aria-label="Furnished living space"></div>Space Planning</div>
    <div class="service"><div class="thumb" style="background:radial-gradient(circle at 40% 35%,#f0d2a8,#c08a55 55%,#7a4e2a)" role="img" aria-label="Home accessories and decor"></div>Accessories and Home Styling</div>
  </div>
</section>

<section class="catalogue">
  <h2 class="section-title">Browse Our Catalouge<span class="title-rule"></span></h2>
  <div class="tabs">
    <span class="active">Furniture Type</span><span>Rooms</span><span>Brands</span><span>Styles</span><span>Material</span><span>Motion Type</span>
  </div>
  <div class="carousel">
    <svg class="arrow" viewBox="0 0 24 24"><path d="M15 4 7 12l8 8" fill="none" stroke="#333" stroke-width="2"/></svg>
    <div class="cat-card"><div class="thumb"><div role="img" aria-label="Sofa"></div></div><p>SOFAS</p></div>
    <div class="cat-card"><div class="thumb"><div role="img" aria-label="Sectional sofa"></div></div><p>SECTIONALS</p></div>
    <div class="cat-card"><div class="thumb"><div role="img" aria-label="Bed"></div></div><p>BEDS</p></div>
    <div class="cat-card"><div class="thumb"><div role="img" aria-label="Dining table with chairs"></div></div><p>TABLE</p></div>
    <svg class="arrow" viewBox="0 0 24 24"><path d="M9 4l8 8-8 8" fill="none" stroke="#333" stroke-width="2"/></svg>
  </div>
</section>

<section class="interiors">
  <h2 class="section-title light">Interior Design<span class="title-rule"></span></h2>
  <div class="interior-list">
    <div class="interior-card"><div class="photo" style="background:radial-gradient(ellipse 60% 50% at 50% 35%,#efe4d4,transparent 70%),linear-gradient(180deg,#c9b8a2 0%,#8e735a 60%,#4e3a2a 100%)" role="img" aria-label="Commercial lounge interior"></div><p>Commercial Design</p></div>
    <div class="interior-card"><div class="photo" style="background:radial-gradient(ellipse 55% 50% at 50% 45%,#f7efe4,transparent 70%),linear-gradient(180deg,#e3d6c4 0%,#b49b80 60%,#6f5843 100%)" role="img" aria-label="Residential living room interior"></div><p>Residencial Design</p></div>
  </div>
  <a class="btn" href="#">View All Interior Design</a>
</section>

<section class="featured">
  <h2 class="section-title">Featured Products<span class="title-rule"></span></h2>
  <div class="product-list">
    <div class="product"><div class="thumb"><div style="background:linear-gradient(180deg,#e4ddd1,#a39581 60%,#6b604f)" role="img" aria-label="Upholstered bench"></div></div><p class="label">BED</p><p class="price"><s>$49.00</s><b>$40.00</b></p><p class="stars">★★★★★</p></div>
    <div class="product"><div class="thumb"><div style="background:linear-gradient(180deg,#5b8dd0,#2f5a96 60%,#1a3358)" role="img" aria-label="Blue lounge chair"></div></div><p class="label">BED</p><p class="price"><s>$49.00</s><b>$40.00</b></p><p class="stars">★★★★★</p></div>
    <div class="product"><div class="thumb"><div style="background:linear-gradient(180deg,#cf5446,#9b2f24 60%,#4f1710)" role="img" aria-label="Red armchair"></div></div><p class="label">BED</p><p class="price"><s>$49.00</s><b>$40.00</b></p><p class="stars">★★★★★</p></div>
    <div class="product"><div class="thumb"><div style="background:linear-gradient(180deg,#86705c,#54412f 60%,#2a1f17)" role="img" aria-label="Round pedestal table"></div></div><p class="label">BED</p><p class="price"><s>$49.00</s><b>$40.00</b></p><p class="stars">★★★★★</p></div>
    <div class="product"><div class="thumb"><div style="background:linear-gradient(180deg,#ddd6cb,#a89e90 60%,#6d6458)" role="img" aria-label="Side chair"></div></div><p class="label">BED</p><p class="price"><s>$49.00</s><b>$40.00</b></p><p class="stars">★★★★★</p></div>
    <div class="product"><div class="thumb"><div style="background:linear-gradient(180deg,#ece6dd,#bfb4a5 60%,#857a6b)" role="img" aria-label="Chaise lounge"></div></div><p class="label">BED</p><p class="price"><s>$49.00</s><b>$40.00</b></p><p class="stars">★★★★★</p></div>
  </div>
</section>

<section class="events">
  <h2 class="section-title">Events<span class="title-rule"></span></h2>
  <div class="event-list">
    <article class="event">
      <div class="photo" style="background:radial-gradient(ellipse 60% 45% at 40% 35%,#e6c79d,transparent 70%),linear-gradient(160deg,#a47b57,#5b3f2a 60%,#2e1f15)" role="img" aria-label="Charity event in a decorated hall"><div class="date">2017<b>21</b>May</div></div>
      <div><h3>Lorem Ipsum is simply dummy text of the printing</h3><p>Lorem Ipsum is simply dummy text of the printing and typesetting industry. Lorem Ipsum has been the industry's standard dummy text ever since the 1500s.</p><a href="#">Read More</a></div>
    </article>
    <article class="event">
      <div class="photo" style="background:radial-gradient(ellipse 60% 45% at 55% 40%,#f0dcc0,transparent 70%),linear-gradient(160deg,#b58d67,#6b4c34 60%,#33241a)" role="img" aria-label="Guests at a fundraising evening"><div class="date">2017<b>21</b>May</div></div>
      <div><h3>Lorem Ipsum is simply dummy text of the printing</h3><p>Lorem Ipsum is simply dummy text of the printing and typesetting industry. Lorem Ipsum has been the industry's standard dummy text ever since the 1500s.</p><a href="#">Read More</a></div>
    </article>
  </div>
  <a class="btn" href="#">View More</a>
</section>

<section class="contact">
  <h2 class="section-title light">Contact Me<span class="title-rule"></span></h2>
  <p class="contact-intro">If you would like to work with the studio, please fill out the form below and a representative will get in touch with you shortly. Please tell us a little about your project so we can prepare. Thank you, we look forward to working with you.</p>
  <div class="form-row">
    <div class="field">Name *</div>
    <div class="field">Email</div>
    <div class="field">Website</div>
    <div class="field select">Residential Design Request <svg width="10" height="8" viewBox="0 0 10 8"><path d="M1 1l4 5 4-5" fill="none" stroke="#fff" stroke-width="1.5"/></svg></div>
  </div>
  <div class="message">Message</div>
  <div class="submit"><a class="btn" href="#">Submit</a></div>
</section>

<footer class="site-footer">
  <div class="social" aria-label="Contact and share links">
    <span><svg width="18" height="14" viewBox="0 0 18 14"><rect x="1" y="1" width="16" height="12" fill="none" stroke="#fff" stroke-width="1.5"/><path d="M1 1l8 7 8-7" fill="none" stroke="#fff" stroke-width="1.5"/></svg></span>
    <span><svg width="16" height="16" viewBox="0 0 16 16"><path d="M3 1h3l1.5 4-2 1.2a9 9 0 0 0 4.3 4.3L11 8.5l4 1.5v3a2 2 0 0 1-2 2A12 12 0 0 1 1 3a2 2 0 0 1 2-2z" fill="#fff"/></svg></span>
    <span><svg width="14" height="18" viewBox="0 0 14 18"><path d="M7 17s6-6.2 6-10.5A6 6 0 0 0 1 6.5C1 10.8 7 17 7 17z" fill="none" stroke="#fff" stroke-width="1.5"/><circle cx="7" cy="6.5" r="2.2" fill="#fff"/></svg></span>
    <span><svg width="18" height="18" viewBox="0 0 18 18"><circle cx="9" cy="9" r="7.5" fill="none" stroke="#fff" stroke-width="1.4"/><ellipse cx="9" cy="9" rx="3.2" ry="7.5" fill="none" stroke="#fff" stroke-width="1.2"/><line x1="1.5" y1="9" x2="16.5" y2="9" stroke="#fff" stroke-width="1.2"/></svg></span>
  </div>
  <p>Copyright © Lorivel Home Studio &nbsp;|&nbsp; All Rights Reserved</p>
</footer>

</body>
</html>
```